Business card and insta posting square

This is for 2 separate projects...

1...a double sided business card for online business (no address) to hand to businesses to get them to list their details on my online directory. the butterfly logo is to be used on the business card.

2.... a posting square for Instagram to write inspirational quotes over the top of to post....with a small butterfly logo somewhere on it (in a corner maybe)....the square is to have a thin, solid green outline around the edge of it, and a faded picture through the background that will allow me to write text over the top of it that will be easily readable.
I would like the same box for all Instagram quote posts for consistency ..

Target Market(s)

spiritual , yoga, meditation, wellness......

Industry/Entity Type

Wellness

Contact Information for Business Card

Details for Business Card...
Wandering The Quiet Tide
Your Complete Wellness Directory
www.wanderingthequiettide.example
insta/FB/pinterest/twitter
*List Your Business for FREE *

Colors
33b8a4
34a7d8
3276b5
876aae
9bcb3c

Requirements
Must have
• butterfly logo included on business card
• insta post square can use the butterfly logo OR the WTQT green square uploaded in the images
Nice to have
• greens

```html
<!DOCTYPE html>
<html lang="en">
<head>
<meta charset="utf-8">
<title>Wandering The Quiet Tide – Business Card</title>
<link href="https://fonts.googleapis.com/css2?family=Montserrat:wght@500;600;700&display=swap" rel="stylesheet">
<style>
  :root {
    --green: #6cbf3c;
    --leaf: #9bcb3c;
    --teal: #1aa3b8;
    --blue: #2f6fb0;
    --purple: #5a2a8a;
    --ink-purple: #5b2d8e;
    --paper: #ffffff;
    --backdrop: #e9e7e4;
  }
  html, body {
    margin: 0;
    width: 1200px;
    height: 900px;
    overflow: hidden;
    background: var(--backdrop);
    font-family: "Montserrat", sans-serif;
  }
  .canvas {
    position: relative;
    width: 1200px;
    height: 900px;
  }
  .card {
    position: absolute;
    left: 290px;
    width: 620px;
    height: 354px;
    border-radius: 4px;
    overflow: hidden;
    box-shadow: 0 6px 18px rgba(0,0,0,0.18);
  }
  .card-front {
    top: 56px;
    background: linear-gradient(135deg, var(--green) 0%, var(--teal) 45%, var(--blue) 72%, var(--purple) 100%);
    display: flex;
    flex-direction: column;
    align-items: center;
    justify-content: center;
    gap: 22px;
  }
  .front-mark {
    width: 110px;
    height: 110px;
    border-radius: 50%;
    background: var(--paper);
  }
  .front-name {
    color: var(--paper);
    font-weight: 600;
    font-size: 32px;
    letter-spacing: 0.5px;
  }
  .card-back {
    top: 474px;
    background: var(--paper);
  }
  .brand-block {
    position: absolute;
    left: 30px;
    top: 22px;
    width: 230px;
    text-align: center;
  }
  .brand-mark {
    display: block;
    width: 64px;
    height: 64px;
    margin: 0 auto 10px;
    border-radius: 50%;
    background: var(--ink-purple);
  }
  .brand-name {
    color: var(--green);
    font-weight: 600;
    font-size: 22px;
    line-height: 1.2;
    margin: 0;
  }
  .brand-tagline {
    color: var(--green);
    font-weight: 600;
    font-size: 11px;
    margin: 6px 0 0;
  }
  .contact-block {
    position: absolute;
    right: 26px;
    top: 48px;
    text-align: right;
  }
  .person-name {
    margin: 0;
    font-weight: 700;
    font-size: 24px;
    color: var(--ink-purple);
  }
  .person-name .surname { color: var(--teal); }
  .person-role {
    margin: 0 0 12px;
    font-weight: 600;
    font-size: 16px;
    color: var(--ink-purple);
  }
  .contact-line {
    display: flex;
    justify-content: flex-end;
    align-items: center;
    gap: 8px;
    margin: 3px 0;
    font-weight: 500;
    font-size: 16px;
    color: var(--ink-purple);
  }
  .contact-line svg { width: 14px; height: 14px; }
  .wave-band {
    position: absolute;
    left: 0;
    bottom: 0;
    width: 620px;
    height: 354px;
  }
  .band-footer {
    position: absolute;
    right: 26px;
    bottom: 14px;
    text-align: right;
    color: var(--paper);
  }
  .social-row {
    display: flex;
    justify-content: flex-end;
    gap: 6px;
    margin-bottom: 8px;
  }
  .social-dot {
    width: 22px;
    height: 22px;
    border-radius: 50%;
    background: var(--paper);
  }
  .free-offer {
    margin: 0;
    font-weight: 500;
    font-size: 18px;
  }
</style>
</head>
<body>
<main class="canvas">

  <section class="card card-front" aria-label="Business card front">
    <span class="front-mark" aria-hidden="true"></span>
    <span class="front-name">Wandering The Quiet Tide</span>
  </section>

  <section class="card card-back" aria-label="Business card back">
    <svg class="wave-band" viewBox="0 0 620 354" aria-hidden="true">
      <defs>
        <linearGradient id="bandGradient" x1="0" y1="0" x2="1" y2="0">
          <stop offset="0" stop-color="#6cbf3c"/>
          <stop offset="0.3" stop-color="#1aa3b8"/>
          <stop offset="0.6" stop-color="#2f6fb0"/>
          <stop offset="1" stop-color="#5a2a8a"/>
        </linearGradient>
      </defs>
      <path d="M0,200 C160,212 330,250 620,196 L620,208 C330,264 160,226 0,216 Z" fill="url(#bandGradient)"/>
      <path d="M0,232 C180,246 360,290 620,222 L620,354 L0,354 Z" fill="url(#bandGradient)"/>
      <path d="M0,252 C200,268 380,306 620,238" fill="none" stroke="#ffffff" stroke-width="6"/>
    </svg>

    <div class="brand-block">
      <span class="brand-mark" aria-hidden="true"></span>
      <p class="brand-name">Wandering The Quiet Tide</p>
      <p class="brand-tagline">Your Complete Wellness Directory</p>
    </div>

    <div class="contact-block">
      <p class="person-name">Maren <span class="surname">Holt</span></p>
      <p class="person-role">Manager</p>
      <p class="contact-line">555-014-2100
        <svg viewBox="0 0 16 16" aria-hidden="true"><path d="M3 1 L6 1 L7 5 L5 6 C6 8 8 10 10 11 L11 9 L15 10 L15 13 C15 14 14 15 13 15 C6 15 1 10 1 3 C1 2 2 1 3 1 Z" fill="#1aa3b8"/></svg>
      </p>
      <p class="contact-line">www.wanderingthequiettide.example
        <svg viewBox="0 0 16 16" aria-hidden="true"><circle cx="8" cy="8" r="7" fill="#2f6fb0"/><path d="M1 8 H15 M8 1 C4 5 4 11 8 15 M8 1 C12 5 12 11 8 15" stroke="#fff" stroke-width="1" fill="none"/></svg>
      </p>
    </div>

    <div class="band-footer">
      <div class="social-row" aria-label="Social profiles">
        <span class="social-dot"></span>
        <span class="social-dot"></span>
        <span class="social-dot"></span>
        <span class="social-dot"></span>
      </div>
      <p class="free-offer">List Your Business for FREE</p>
    </div>
  </section>

</main>
</body>
</html>
```